Option Sheet

We need a one page option sheet with a left to right reading of the five options. It should be a one sheet, multiple colors and definitive separations between options This is used in a sales consultation. Backround or colors not in option need to have the follow RGB value (5 red, 20 green, 63 blue)

We added a smaller text file, please change that point

Target Market(s)

Divorce

Industry/Entity Type

Legal

Requirements
Must have
• 1) All five options left to right
• 2)language included in sheet

```html
<!DOCTYPE html>
<html lang="en">
<head>
<meta charset="utf-8">
<title>Five Options Divorce</title>
<link href="https://fonts.googleapis.com/css2?family=Barlow:wght@700&family=Arimo:wght@400;700&display=swap" rel="stylesheet">
<style>
  :root {
    --navy: rgb(5, 20, 63);
    --white: #ffffff;
    --o1-tab: #00477a; --o1-band: #286c9e; --o1-body: #618caf;
    --o2-tab: #0b759c; --o2-band: #0088c1; --o2-body: #5ca3bf;
    --o3-tab: #2b95ac; --o3-band: #47b0c6; --o3-body: #97c9da;
    --o4-tab: #745da6; --o4-band: #8a7bb0; --o4-body: #bbafd6;
    --o5-tab: #4f5b9b; --o5-band: #6574b1; --o5-body: #8f9bbf;
  }
  * { margin: 0; padding: 0; box-sizing: border-box; }
  html, body { width: 927px; height: 1200px; overflow: hidden; background: var(--navy); }
  .sheet { position: relative; width: 927px; height: 1200px; color: var(--white); font-family: "Arimo", Arial, sans-serif; }

  .sheet-header { height: 65px; background: var(--navy); display: flex; align-items: center; justify-content: center; }
  .sheet-title { font-family: "Barlow", sans-serif; font-weight: 700; font-size: 31px; padding-left: 10px; }

  .option-band { position: relative; height: 34px; }
  .option-band svg { position: absolute; left: 0; top: 0; }
  .option-number, .option-name { position: absolute; top: 0; line-height: 34px; font-family: "Barlow", sans-serif; font-weight: 700; font-size: 17px; }

  .option-body { display: flex; }
  .col { position: relative; }
  .col-adv { width: 466px; padding-left: 57px; }
  .col-dis { width: 461px; padding-right: 22px; }
  .col-heading { font-weight: 700; font-size: 18px; line-height: 25px; }
  .points { list-style: none; }
  .points li { position: relative; padding-left: 23px; font-size: 18px; line-height: 25px; }
  .points li::before { content: ""; position: absolute; left: 4px; top: 10px; width: 6px; height: 6px; border-radius: 50%; background: var(--white); }

  .opt1 .option-band { background: var(--o1-band); } .opt1 .option-body { background: var(--o1-body); height: 128px; padding-top: 9px; }
  .opt2 .option-band { background: var(--o2-band); } .opt2 .option-body { background: var(--o2-body); height: 201px; padding-top: 9px; }
  .opt3 .option-band { background: var(--o3-band); } .opt3 .option-body { background: var(--o3-body); height: 204px; padding-top: 8px; }
  .opt4 .option-band { background: var(--o4-band); } .opt4 .option-body { background: var(--o4-body); height: 250px; padding-top: 8px; border-bottom: 1px solid #d7d0e6; }
  .opt5 .option-band { background: var(--o5-band); } .opt5 .option-body { background: var(--o5-body); height: 183px; padding-top: 8px; }

  .opt2 .col-adv { padding-top: 7px; }
  .opt2 .col-dis, .opt3 .col-dis, .opt4 .col-dis { padding-left: 3px; }
  .opt4 .col-adv .points { max-width: 250px; }
  .opt5 .col-dis { padding-left: 9px; }
  .opt5 .col-dis .points li { padding-left: 28px; }
</style>
</head>
<body>
<main class="sheet">
  <header class="sheet-header"><h1 class="sheet-title">Five Options Divorce</h1></header>

  <section class="option opt1">
    <div class="option-band">
      <svg width="270" height="34" aria-hidden="true"><polygon points="0,0 257,0 266,17 257,34 0,34" fill="var(--o1-tab)"/></svg>
      <span class="option-number" style="left:77px">Option #1</span>
      <span class="option-name" style="left:492px">Do Nothing</span>
    </div>
    <div class="option-body">
      <div class="col col-adv"><h2 class="col-heading">Advantages:</h2>
        <ul class="points"><li>Stay married</li><li>No life Changes</li></ul></div>
      <div class="col col-dis"><h2 class="col-heading">Disadvantages:</h2>
        <ul class="points"><li>Remain unhappy, depressed, anxious</li><li>Money and assets may disappear</li><li>What is going to change?</li></ul></div>
    </div>
  </section>

  <section class="option opt2">
    <div class="option-band">
      <svg width="270" height="34" aria-hidden="true"><polygon points="0,0 255,0 264,17 255,34 0,34" fill="var(--o2-tab)"/></svg>
      <span class="option-number" style="left:69px">Option #2</span>
      <span class="option-name" style="left:468px">Go to Counseling</span>
    </div>
    <div class="option-body">
      <div class="col col-adv"><h2 class="col-heading">Advantages:</h2>
        <ul class="points"><li>Reconcile Marriage</li><li>&nbsp;Help make a better life</li></ul></div>
      <div class="col col-dis"><h2 class="col-heading">Disadvantages:</h2>
        <ul class="points"><li>Past issues are highlighted and may drudge up old wounds</li><li>It may just clarify the reasons you need to separate and/or divorce</li><li>Both parties mustbe invested and willing to participate</li></ul></div>
    </div>
  </section>

  <section class="option opt3">
    <div class="option-band">
      <svg width="270" height="34" aria-hidden="true"><polygon points="0,0 255,0 264,17 255,34 0,34" fill="var(--o3-tab)"/></svg>
      <span class="option-number" style="left:69px">Option #3</span>
      <span class="option-name" style="left:493px">Do it Yourself</span>
    </div>
    <div class="option-body">
      <div class="col col-adv"><h2 class="col-heading">Advantages:</h2>
        <ul class="points"><li>No attorney fees</li><li>You are your own attorney</li></ul></div>
      <div class="col col-dis"><h2 class="col-heading">Disadvantages:</h2>
        <ul class="points"><li>People often find that what is “fair,” may in fact, not be truly fair</li><li>Often times, people do not know the risks</li><li>Complicated legal system</li><li>Unsure how to complete the necessary paperwork and meet the deadlines</li></ul></div>
    </div>
  </section>

  <section class="option opt4">
    <div class="option-band">
      <svg width="270" height="34" aria-hidden="true"><polygon points="0,0 255,0 264,17 255,34 0,34" fill="var(--o4-tab)"/></svg>
      <span class="option-number" style="left:79px">Option #4</span>
      <span class="option-name" style="left:453px">Limited Representation</span>
    </div>
    <div class="option-body">
      <div class="col col-adv"><h2 class="col-heading">Advantages:</h2>
        <ul class="points"><li>Balance between going alone and our limited involvement in the case</li></ul></div>
      <div class="col col-dis"><h2 class="col-heading">Disadvantages:</h2>
        <ul class="points"><li>Our terms may not benefit from our legal knowledge</li><li>The legal consequences of your legal documents will not be explained to you so that you can formulate a plan for handling the rest of your case</li><li>Your spouse or other parties may cause your legal fees to increase significantly without action on your part</li></ul></div>
    </div>
  </section>

  <section class="option opt5">
    <div class="option-band">
      <svg width="270" height="34" aria-hidden="true"><polygon points="0,0 255,0 264,17 255,34 0,34" fill="var(--o5-tab)"/></svg>
      <span class="option-number" style="left:83px">Option #5</span>
      <span class="option-name" style="left:531px">Hire Us</span>
    </div>
    <div class="option-body">
      <div class="col col-adv"><h2 class="col-heading">Advantages:</h2>
        <ul class="points"><li>Gain the full benefits of our experience</li><li>Have a team of Family Law focus attorneys</li><li>Often saves you or makes you money in the long run</li><li>Save you time, energy and stress</li></ul></div>
      <div class="col col-dis"><h2 class="col-heading">Disadvantages:</h2>
        <ul class="points"><li>Initial cost</li></ul></div>
    </div>
  </section>
</main>
</body>
</html>
```